Veterinary Business cards

Redesign Business Card

Information needed on Card:
Hours: Mon-Fri: 4pm -10PM; Sat- Sun- 10 AM- 5PM
Help@bayfernvet.com
www.bayfernvet.com
555-718-2946
4173 SE 19th Ave. okc, ok 73958
*No appointment necessary*

Optional:
Our tag line is "We're here when you need us" - If it fits on the cards.

```html
<!DOCTYPE html>
<html lang="en">
<head>
<meta charset="utf-8">
<title>Bayfern Vet Urgent Care – Business Cards</title>
<link href="https://fonts.googleapis.com/css2?family=Arimo:wght@400;700&family=Archivo+Black&display=swap" rel="stylesheet">
<style>
  :root {
    --backdrop: #1c1c1e;
    --card: #111112;
    --brand-blue: #1d3f6e;
    --brand-blue-text: #3a6db3;
    --accent-orange: #e0851f;
    --text-light: #f4f4f4;
  }
  * { box-sizing: border-box; margin: 0; padding: 0; }
  html, body { width: 1200px; height: 900px; overflow: hidden; }
  body {
    background: var(--backdrop);
    font-family: "Arimo", Arial, sans-serif;
    display: flex; flex-direction: column; align-items: center;
    justify-content: center; gap: 36px;
  }
  .card {
    position: relative;
    width: 720px; height: 400px;
    background: var(--card);
    border-bottom: 12px solid var(--brand-blue);
    box-shadow: 0 10px 30px rgba(0,0,0,.6);
    overflow: hidden;
  }
  .brand-name {
    position: absolute; left: 0; right: 0;
    display: flex; align-items: center; justify-content: center; gap: 14px;
    color: var(--brand-blue-text);
    font-family: "Arimo", Arial, sans-serif;
    font-weight: 400; letter-spacing: 2px; text-transform: uppercase;
    white-space: nowrap;
  }
  .brand-dot { flex: none; width: 22px; height: 22px; border-radius: 50%; background: var(--accent-orange); }

  /* front */
  .card-front .brand-name { top: 130px; font-size: 40px; }
  .tagline {
    position: absolute; top: 215px; left: 0; right: 0; text-align: center;
    font-family: "Archivo Black", Arial, sans-serif;
    color: var(--accent-orange); font-size: 28px; letter-spacing: 1.5px;
  }
  .walk-in {
    position: absolute; left: 0; right: 0; text-align: center;
    color: var(--text-light); font-size: 18px; font-style: italic;
  }
  .card-front .walk-in { top: 275px; }

  /* back */
  .card-back .brand-name { top: 48px; font-size: 36px; }
  .contact-list {
    position: absolute; top: 140px; right: 380px;
    list-style: none; text-align: right; color: var(--text-light);
    font-size: 19px; line-height: 30px;
  }
  .contact-list li { display: flex; align-items: center; justify-content: flex-end; gap: 8px; }
  .icon { width: 18px; height: 18px; fill: none; stroke: var(--accent-orange); stroke-width: 2; }
  .icon-solid { fill: var(--accent-orange); stroke: none; }
  .divider {
    position: absolute; top: 138px; left: 358px; width: 2px; height: 96px;
    background: var(--brand-blue-text);
  }
  .hours {
    position: absolute; top: 145px; left: 384px;
    color: var(--text-light); font-size: 19px; line-height: 27px;
  }
  .hours-title { color: var(--accent-orange); font-weight: 700; font-size: 20px; }
  .address {
    position: absolute; top: 265px; left: 0; right: 0;
    display: flex; justify-content: center; align-items: center; gap: 8px;
    color: var(--text-light); font-size: 20px;
  }
  .card-back .walk-in { top: 318px; }
</style>
</head>
<body>
  <section class="card card-front">
    <div class="brand-name"><span class="brand-dot"></span>Bayfern Vet Urgent Care</div>
    <p class="tagline">WE'RE HERE WHEN YOU NEED US</p>
    <p class="walk-in">*No appointment necessary*</p>
  </section>

  <section class="card card-back">
    <div class="brand-name"><span class="brand-dot"></span>Bayfern Vet Urgent Care</div>
    <ul class="contact-list">
      <li>555-718-2946
        <svg class="icon" viewBox="0 0 24 24"><path d="M5 3h4l2 5-2.5 1.5a11 11 0 0 0 6 6L16 13l5 2v4a2 2 0 0 1-2 2A16 16 0 0 1 3 5a2 2 0 0 1 2-2z"/></svg></li>
      <li>Help@bayfernvet.com
        <svg class="icon" viewBox="0 0 24 24"><rect x="3" y="5" width="18" height="14"/><path d="M3 5l9 8 9-8"/></svg></li>
      <li>www.bayfernvet.com
        <svg class="icon" viewBox="0 0 24 24"><circle cx="12" cy="12" r="9"/><path d="M3 12h18M12 3c3 3 3 15 0 18M12 3c-3 3-3 15 0 18"/></svg></li>
    </ul>
    <div class="divider"></div>
    <div class="hours">
      <p class="hours-title">Hours:</p>
      <p>Mon-Fri: 4pm -10PM;</p>
      <p>Sat- Sun- 10 AM- 5PM</p>
    </div>
    <p class="address">
      <svg class="icon icon-solid" viewBox="0 0 24 24"><path d="M12 2a7 7 0 0 0-7 7c0 5 7 13 7 13s7-8 7-13a7 7 0 0 0-7-7zm0 9.5A2.5 2.5 0 1 1 12 6.5a2.5 2.5 0 0 1 0 5z"/></svg>
      4173 SE 19th Ave. okc, ok 73958
    </p>
    <p class="walk-in">*No appointment necessary*</p>
  </section>
</body>
</html>
```